Flyer Design

I will be hosting an event at Penrith's amber lantern. Here is a link to their page http://www.theamberlantern.com.au/events-and-workshops/whats-on-penrith/. I have attached the details of my course from their website below. I hope this is of some valuable assistance.

Florist and lover of all things gorgeous, Molly Hartwell from Molly Hartwell Flowers will be running this beautiful and fun workshop. Come along to learn how to make your very own floral crown. All you need to bring are some closed in shoes, an apron and an open mind ready for creativity!

Teens & adults welcome

Date 1: Saturday 11 April 2015
Time 1: 11:00-2:00pm

Date 2: Thursday 23 April 2015
Time 2: 6:00-9:00pm

Cost: $90 per person (includes materials provided – see list below)
Place: The Amber Lantern, Unit 3, 27 Baxter Lane Penrith
RSVP: Molly via email mollyhartwellflowers@fernmail.example or phone 0431 795 206

Materials provided:
• Florist scissors
• Floral tape
• Wire
• Flowers
• light snacks & refreshments

```html
<!DOCTYPE html>
<html lang="en">
<head>
<meta charset="utf-8">
<title>Floral Crowns Workshop Flyer</title>
<link rel="stylesheet" href="https://fonts.googleapis.com/css2?family=Roboto+Condensed:wght@300;400;700&family=Lato:wght@400;700&family=Marcellus&display=swap">
<style>
  :root {
    --pink: #e8398a;
    --green: #a8c839;
    --yellow: #ffe100;
    --cyan: #27b8dc;
    --purple: #6b2d8c;
    --ink: #2b2b2b;
    --white: #ffffff;
    --photo-light: #ece7de;
    --photo-dark: #b9b3a4;
  }
  * { margin: 0; padding: 0; box-sizing: border-box; }
  html, body { width: 920px; height: 1200px; overflow: hidden; background: var(--white); }
  .flyer { position: relative; width: 920px; height: 1200px; overflow: hidden; font-family: "Lato", sans-serif; color: var(--ink); }
  .flyer__shapes { position: absolute; inset: 0; }

  .price { position: absolute; left: 26px; top: 484px; display: flex; align-items: center; gap: 14px; }
  .price__amount { font-family: "Roboto Condensed", sans-serif; font-weight: 700; font-size: 86px; line-height: 1; color: var(--purple); letter-spacing: -2px; }
  .price__unit { font-family: "Roboto Condensed", sans-serif; font-weight: 400; font-size: 29px; line-height: 1; color: var(--white); }

  .session { position: absolute; font-family: "Roboto Condensed", sans-serif; font-weight: 700; }
  .session__date { font-size: 22px; line-height: 1; }
  .session__time { font-size: 40px; line-height: 1; color: var(--cyan); margin-top: 6px; }
  .session--one { left: 26px; top: 614px; color: var(--white); }
  .session--two { right: 490px; top: 704px; text-align: right; color: var(--purple); }

  .welcome { position: absolute; right: 490px; top: 812px; text-align: right; font-family: "Roboto Condensed", sans-serif; font-weight: 300; line-height: 1; }
  .welcome__line1 { font-size: 44px; color: var(--white); }
  .welcome__line2 { font-size: 54px; color: var(--purple); margin-top: 2px; }

  .contact { position: absolute; left: 40px; top: 1010px; list-style: none; color: var(--white); font-size: 21px; line-height: 1.3; }
  .contact li { display: flex; align-items: flex-start; gap: 12px; margin-bottom: 18px; }
  .contact svg { flex: none; margin-top: 4px; }

  .brand { position: absolute; left: 600px; top: 492px; font-family: "Roboto Condensed", sans-serif; font-weight: 700; font-size: 30px; line-height: 1; color: var(--white); white-space: nowrap; }

  .title { position: absolute; left: 484px; top: 688px; }
  .title__top { font-family: "Roboto Condensed", sans-serif; font-weight: 700; font-size: 42px; line-height: 1; color: var(--cyan); }
  .title__bottom { font-family: "Marcellus", serif; font-weight: 400; font-size: 46px; line-height: 1; color: var(--ink); margin-top: 4px; }

  .intro { position: absolute; left: 484px; top: 794px; width: 414px; font-size: 16.5px; line-height: 1.28; text-align: justify; color: var(--ink); }

  .materials__title { position: absolute; left: 476px; top: 938px; font-family: "Roboto Condensed", sans-serif; font-weight: 700; font-size: 25px; color: var(--white); }
  .materials__list { position: absolute; top: 994px; list-style: none; font-size: 17px; font-weight: 700; line-height: 1.3; }
  .materials__list li { margin-bottom: 10px; padding-left: 14px; position: relative; }
  .materials__list li::before { content: ""; position: absolute; left: 0; top: 8px; width: 7px; height: 7px; border-radius: 50%; background: var(--pink); }
  .materials__list--a { left: 476px; }
  .materials__list--b { left: 712px; }

  .web { position: absolute; right: 26px; top: 1125px; font-family: "Roboto Condensed", sans-serif; font-weight: 700; font-size: 19px; color: var(--white); }
</style>
</head>
<body>
<main class="flyer">
  <svg class="flyer__shapes" width="920" height="1200" viewBox="0 0 920 1200">
    <defs>
      <linearGradient id="photoTone" x1="0" y1="0" x2="1" y2="1">
        <stop offset="0" stop-color="var(--photo-light)"/>
        <stop offset="0.6" stop-color="#d8d3c6"/>
        <stop offset="1" stop-color="var(--photo-dark)"/>
      </linearGradient>
    </defs>
    <polygon class="hero-photo" role="img" aria-label="Photo of the florist smiling in her studio among potted plants and red flowers" points="0,0 920,0 920,258 441,452 0,295" fill="url(#photoTone)"/>
    <polygon class="stripe-cyan-top" points="0,247 410,440 404,458 0,265" fill="var(--cyan)"/>
    <polygon class="accent-pink" points="426,449 920,258 920,672 455,482" fill="var(--pink)"/>
    <polygon class="stripe-cyan-mid" points="462,496 920,686 920,702 458,510" fill="var(--cyan)"/>
    <polygon class="panel-green" points="0,295 466,465 466,1027 0,865" fill="var(--green)"/>
    <polygon class="stripe-white" points="0,322 466,492 466,500 0,330" fill="var(--white)"/>
    <polygon class="stripe-yellow" points="0,340 466,510 466,530 0,360" fill="var(--yellow)"/>
    <rect class="band-pink" x="0" y="600" width="466" height="92" fill="var(--pink)"/>
    <rect class="band-yellow" x="0" y="692" width="458" height="92" fill="var(--yellow)"/>
    <polygon class="stripe-yellow-low" points="0,884 466,1046 466,1064 0,902" fill="var(--yellow)"/>
    <polygon class="panel-cyan" points="0,935 764,1200 0,1200" fill="var(--cyan)"/>
    <polygon class="materials-bar" points="456,932 768,932 784,976 456,976" fill="var(--green)"/>
    <polygon class="web-bar" points="552,1117 920,1117 920,1160 580,1160" fill="var(--green)"/>
  </svg>

  <div class="price"><span class="price__amount">$90</span><span class="price__unit">PER<br>PERSON</span></div>

  <div class="session session--one">
    <div class="session__date">SATURDAY 11 APRIL 2015</div>
    <div class="session__time">11:00-2:00PM</div>
  </div>
  <div class="session session--two">
    <div class="session__date">THURSDAY 23 APRIL 2015</div>
    <div class="session__time">6:00-9:00PM</div>
  </div>

  <div class="welcome">
    <div class="welcome__line1">TEENS &amp; ADULTS</div>
    <div class="welcome__line2">WELCOME</div>
  </div>

  <ul class="contact">
    <li>
      <svg width="18" height="18" viewBox="0 0 24 24"><path d="M6.6 10.8a15 15 0 0 0 6.6 6.6l2.2-2.2a1 1 0 0 1 1-.25 11.4 11.4 0 0 0 3.6.57 1 1 0 0 1 1 1V20a1 1 0 0 1-1 1A17 17 0 0 1 3 4a1 1 0 0 1 1-1h3.5a1 1 0 0 1 1 1c0 1.25.2 2.45.57 3.57a1 1 0 0 1-.25 1z" fill="var(--yellow)"/></svg>
      <span>0431 795 206</span>
    </li>
    <li>
      <svg width="18" height="20" viewBox="0 0 24 24"><path d="M12 2a7 7 0 0 0-7 7c0 5.2 7 13 7 13s7-7.8 7-13a7 7 0 0 0-7-7zm0 9.5A2.5 2.5 0 1 1 12 6.5a2.5 2.5 0 0 1 0 5z" fill="var(--yellow)"/></svg>
      <span>The Amber Lantern,<br>Unit 3, 27 Baxter Lane Penrith</span>
    </li>
    <li>
      <svg width="18" height="16" viewBox="0 0 24 20"><path d="M2 2h20v16H2z" fill="var(--yellow)"/><path d="M2 2l10 8 10-8" fill="none" stroke="var(--cyan)" stroke-width="2"/></svg>
      <span>mollyhartwellflowers@fernmail.example</span>
    </li>
  </ul>

  <div class="brand">THE AMBER LANTERN</div>

  <h1 class="title">
    <div class="title__top">FLORAL CROWNS</div>
    <div class="title__bottom">WORKSHOP</div>
  </h1>

  <p class="intro">Florist and lover of all things gorgeous, Molly Hartwell from Molly Hartwell Flowers will be running this beautiful and fun workshop. Come along to learn how to make your very own floral crown. All you need to bring are some closed in shoes, an apron and an open mind ready for creativity!</p>

  <h2 class="materials__title">MATERIALS PROVIDED</h2>
  <ul class="materials__list materials__list--a">
    <li>Florist scissors</li>
    <li>Floral tape</li>
    <li>Wire</li>
  </ul>
  <ul class="materials__list materials__list--b">
    <li>Flowers</li>
    <li>light snacks &amp;<br>refreshments</li>
  </ul>

  <div class="web">www.theamberlantern.com.au</div>
</main>
</body>
</html>
```